Venture Capital Investment Firm

We are looking to overhaul our existing website (substantially), with only using the same logos (which we can provide).
We are an investment firm that focuses on making loans to late stage technology companies. Our site should ultimately look like other venture capital firms, and look modern and fresh. We have an existing website www.northvaleloan.com which this will be replacing, although we will be using a lot of the existing written content, and potentially the numbers of pages we will need, we are not wed to anything else. Please feel free to shoot any questions at any time and thank you in advance for your help!
Websites we like as examples:
https://www.tkbrandel.com/
https://www.emberwoodfunds.com/
Target Market(s)
Potential investors who will invest in our firm, as well as potentially companies that are looking to borrow money from us.

```html
<!DOCTYPE html>
<html lang="en">
<head>
<meta charset="utf-8">
<title>Northvale IP — Partners For Growth</title>
<link rel="stylesheet" href="https://fonts.googleapis.com/css2?family=Raleway:wght@300;400;500;600&display=swap">
<style>
:root{
  --navy:#1d2847;
  --teal:#2a6479;
  --accent:#5d9bb6;
  --gold:#ecd7a0;
  --ink:#6f7680;
  --panel:#f5f7f9;
  --band:#f4f6f8;
  --white:#ffffff;
}
*{margin:0;padding:0;box-sizing:border-box}
html,body{width:1200px;height:4866px;overflow:hidden}
body{position:relative;background:var(--white);font-family:"Raleway",sans-serif;color:var(--ink)}
.abs{position:absolute}
p{font-size:11.5px;line-height:20px;font-weight:400;color:var(--ink)}
p+p{margin-top:12px}

/* header / hero */
.hero{left:0;top:0;width:1200px;height:548px;
  background:linear-gradient(180deg,#6fa4c4 0%,#a9cbe0 30%,#d8e6ee 56%,#c9d2d6 66%,#6d6b6a 76%,#3f3b3a 88%,#2b2726 100%)}
.brand{left:151px;top:24px;display:flex;align-items:center;gap:12px}
.brand-mark{width:30px;height:30px;border-radius:50%;background:var(--navy)}
.brand-name{font-size:22px;font-weight:500;color:var(--navy);letter-spacing:1px}
.nav{left:399px;top:36px}
.nav a{position:absolute;font-size:9.5px;letter-spacing:1px;color:#3e5168;text-decoration:none;white-space:nowrap}
.nav a.active{text-decoration:underline}
.login{left:907px;top:23px;width:142px;height:39px;border:1.5px solid #4a5a70;border-radius:20px;
  font-size:9.5px;letter-spacing:1px;color:#3e5168;display:flex;align-items:center;justify-content:center}
.hero-title{left:0;width:1200px;top:214px;text-align:center;font-size:41px;font-weight:400;color:var(--navy)}
.hero-sub{left:0;width:1200px;top:274px;text-align:center;font-size:15px;line-height:23px;color:#34475e;font-weight:400}

.vline{width:2px;background:#a8c6d6;left:599px}

.section-title{font-size:29px;font-weight:500;color:var(--navy)}
.gold-rule{height:2px;width:55px;background:var(--gold)}

/* feature rows */
.photo{box-shadow:0 6px 14px rgba(0,0,0,.18)}
.feature-panel{background:var(--panel)}
.feature-title{font-size:22px;font-weight:400;color:var(--teal);letter-spacing:.5px}
.bar{width:3px;background:var(--accent)}

/* transactions */
.band{left:0;top:1833px;width:1200px;height:599px;background:var(--band)}
.type{width:220px;text-align:center}
.type-circle{width:132px;height:132px;border-radius:50%;background:var(--white);margin:0 auto;
  box-shadow:0 2px 8px rgba(0,0,0,.06);display:flex;align-items:center;justify-content:center}
.type-art{width:64px;height:64px;border-radius:50%}
.type-label{margin-top:36px;font-size:17px;color:var(--teal);font-weight:400;letter-spacing:.4px;white-space:nowrap}

/* benefit cards */
.card{left:151px;width:898px;background:var(--white);box-shadow:0 3px 14px rgba(0,0,0,.1);overflow:hidden}
.card-bar{left:0;top:0;width:3px;height:62px;background:var(--accent)}
.card-photo{right:0;top:0;height:100%;width:380px}
.card-body{left:76px;width:540px}
.card-title{font-size:22px;font-weight:500;color:var(--teal);letter-spacing:.5px;margin-bottom:22px}
.card-body p{font-size:10.5px;line-height:19px}
.card-body p+p{margin-top:11px}

.btn{left:503px;top:4292px;width:193px;height:42px;border:1.5px solid var(--navy);border-radius:22px;
  font-size:12px;color:var(--navy);display:flex;align-items:center;justify-content:center}

/* footer */
.footer{left:0;top:4523px;width:1200px;height:343px;
  background:linear-gradient(180deg,#1f4a5a 0%,#2b5b6b 40%,#1b3f4d 75%,#163240 100%)}
.footer-brand{left:0;width:1200px;top:4628px;display:flex;justify-content:center;align-items:center;gap:14px}
.footer-brand .brand-mark{width:44px;height:44px;background:var(--white)}
.footer-brand .brand-name{font-size:40px;color:var(--white);font-weight:400}
.footer-nav a{position:absolute;top:4729px;font-size:9.5px;letter-spacing:1px;color:#dbe6ea;text-decoration:none}
.legal{left:0;width:1200px;text-align:center;font-size:7px;line-height:12px;color:#cfdce1}
</style>
</head>
<body>

<header>
  <div class="abs hero" role="img" aria-label="Aerial photo of a city skyline and waterfront under a pale blue sky"></div>
  <div class="abs brand"><span class="brand-mark"></span><span class="brand-name">NORTHVALE IP</span></div>
  <nav class="abs nav">
    <a class="active" style="left:0">STRATEGY</a>
    <a style="left:111px">ABOUT US</a>
    <a style="left:225px">TEAM</a>
    <a style="left:310px">NEWS</a>
    <a style="left:399px">CONTACT</a>
  </nav>
  <div class="abs login">INVESTORS LOGIN</div>
  <h1 class="abs hero-title">Partners For Growth</h1>
  <div class="abs hero-sub">We Provide Flexible Capital to Innovative Companies<br>and Their Investors</div>
</header>

<div class="abs vline" style="top:548px;height:42px"></div>

<section>
  <h2 class="abs section-title" style="left:225px;top:656px">Industry Focus</h2>
  <div class="abs gold-rule" style="left:225px;top:738px"></div>
  <div class="abs" style="left:534px;top:658px;width:430px">
    <p>Our focus spans the life science and technology industries, two sectors where intellectual property (IP) is an integral driver of asset and enterprise value.</p>
    <p>Our broad experience in investing, technology evaluation, and product forecasting affords us a unique understanding of the value of assets in these dynamic sectors, allowing us to see value where others cannot.</p>
  </div>

  <div class="abs feature-panel" style="left:688px;top:898px;width:361px;height:277px"></div>
  <div class="abs bar" style="left:1046px;top:898px;height:62px"></div>
  <div class="abs photo" role="img" aria-label="Pipette dispensing pink liquid into a laboratory well plate" style="left:151px;top:852px;width:537px;height:367px;background:linear-gradient(135deg,#3a3d44 0%,#8d939c 40%,#c7ccd2 60%,#4d4f57 100%)"></div>
  <h3 class="abs feature-title" style="left:741px;top:956px">Life Sciences</h3>
  <div class="abs" style="left:741px;top:1000px;width:265px"><p>We have a long track record of partnering with companies and investors that create and commercialize life science products, with extensive experience spanning biopharmaceuticals, medical devices, and tools &amp; diagnostics.</p></div>

  <div class="abs feature-panel" style="left:151px;top:1355px;width:359px;height:221px"></div>
  <div class="abs bar" style="left:151px;top:1355px;height:62px"></div>
  <div class="abs photo" role="img" aria-label="Close-up of a circuit board in a manufacturing machine" style="left:510px;top:1310px;width:539px;height:364px;background:linear-gradient(180deg,#d9dadb 0%,#8b8c8e 30%,#2e2f31 65%,#111214 100%)"></div>
  <h3 class="abs feature-title" style="left:204px;top:1413px">Technology</h3>
  <div class="abs" style="left:204px;top:1458px;width:255px"><p>We uniquely offer sizeable and flexible structured credit financing solutions to innovative technology companies, with a focus on enterprise software, data &amp; analytics, semiconductors, and communications systems.</p></div>
</section>

<section>
  <div class="abs band"></div>
  <div class="abs vline" style="top:1767px;height:81px"></div>
  <h2 class="abs section-title" style="left:0;width:1200px;text-align:center;top:1908px">Transaction Types</h2>
  <div class="abs gold-rule" style="left:573px;top:1968px"></div>
  <div class="abs" style="left:227px;top:2010px;width:745px">
    <p>Northvale IP's proven strategy focuses on identifying opportunities where demonstrated commercial success has established underlying asset or enterprise value prior to our investment. We tailor our financing solutions to each situation with the goal of preserving our partners' ownership interests, aligning incentives, and providing operating flexibility to build businesses of value.</p>
    <p>Our approach enables us to work flexibly to meet the needs of companies, investors, and entrepreneurs we partner with through a wide array of transaction structures.</p>
  </div>
  <div class="abs type" style="left:240px;top:2170px">
    <div class="type-circle"><div class="type-art" role="img" aria-label="Illustration of a stack of coins" style="background:radial-gradient(circle,#5cc2c0 0%,#3fa3a6 55%,#e6eef0 100%)"></div></div>
    <div class="type-label">Structured Credit</div>
  </div>
  <div class="abs type" style="left:490px;top:2170px">
    <div class="type-circle"><div class="type-art" role="img" aria-label="Illustration of a ring of coins" style="background:radial-gradient(circle,#e6f2f2 0%,#7cc3c3 55%,#eaf1f2 100%)"></div></div>
    <div class="type-label">Milestones &amp; Royalties</div>
  </div>
  <div class="abs type" style="left:739px;top:2170px">
    <div class="type-circle"><div class="type-art" role="img" aria-label="Illustration of falling gold coins" style="background:radial-gradient(circle,#f0d56a 0%,#f3dc7c 50%,#faf4e0 100%)"></div></div>
    <div class="type-label">Legacy Assets</div>
  </div>
</section>

<div class="abs vline" style="top:2523px;height:85px"></div>

<section>
  <h2 class="abs section-title" style="left:225px;top:2674px">Key Benefits</h2>
  <div class="abs gold-rule" style="left:225px;top:2758px"></div>
  <div class="abs" style="left:534px;top:2676px;width:430px">
    <p>We seek to fill a void in the capital markets where too often complexity and perceived risk penalize innovative companies with proven products. We apply our team's deep domain knowledge to identify situations where our structured financing alternatives can deliver a lower cost of capital than traditional venture capital or growth equity and allow our transaction partners to avoid significant dilution at sub-optimal valuations.</p>
    <p>We also target situations where venture loans and commercial banks are not attractive or viable options given the limited amount of debt capital offered, near-term principal amortization, requirements for substantial liquidity after investment, and the regimented criteria these lenders often focus on prior to extending credit.</p>
  </div>

  <article class="abs card" style="top:2990px;height:440px">
    <div class="abs card-photo" role="img" aria-label="Faded photo of a twisting glass skyscraper" style="background:linear-gradient(90deg,#ffffff 0%,#f1f3f5 40%,#cdd3d8 75%,#aab3ba 100%)"></div>
    <div class="abs card-bar"></div>
    <div class="abs card-body" style="top:60px">
      <h3 class="card-title">Structured Credit</h3>
      <p>We offer revenue-generating companies in the life science and technology industries bespoke loans which offer multiple benefits.</p>
      <p>• Sizeable: $10-250M+<br>• Flexible: Long-term maturity dates<br>• Efficient: Minimally dilutive</p>
      <p>Structured credit offers an attractive financing alternative that allows companies to reach value inflection prior to a sale, IPO, or equity financing in order to maximize investor return. Fundamentally different than venture debt, our facilities are long-term, typically without amortization of principal prior to maturity.</p>
      <p>Our financings are designed to allow our transaction partners to realize the value of businesses they have built. We recognize that proprietary assets generating high margins are highly sought after by strategic buyers and represent collateral that can be unlocked in ways that are under-appreciated by traditional lenders.</p>
    </div>
  </article>

  <article class="abs card" style="top:3464px;height:331px">
    <div class="abs card-photo" role="img" aria-label="Faded photo of a stone clock tower" style="background:linear-gradient(90deg,#ffffff 0%,#eceeef 40%,#b9bbbd 75%,#97999b 100%)"></div>
    <div class="abs card-bar"></div>
    <div class="abs card-body" style="top:58px">
      <h3 class="card-title">Milestones &amp; Royalties</h3>
      <p>We offer owners of milestones &amp; royalty rights the ability to monetize or securitize future cash flows ranging from $10-250M.</p>
      <p>Northvale IP has the ability to structure its transactions in a variety of ways depending on the specific attributes of milestone &amp; royalty payments and the funding requirements and circumstances of each royalty recipient – whether an inventor, university, research institute, hospital, or company.</p>
      <p>Quantifying and appropriately valuing payment streams created through the licensing of IP is a core strength of our team and we work closely with royalty recipients to understand their entitlements and create an optimal financial structure.</p>
    </div>
  </article>

  <article class="abs card" style="top:3831px;height:369px">
    <div class="abs card-photo" role="img" aria-label="Faded photo of a rocket on a launch pad" style="background:linear-gradient(90deg,#ffffff 0%,#f0f3f5 40%,#d3d9de 75%,#b2bcc3 100%)"></div>
    <div class="abs card-bar"></div>
    <div class="abs card-body" style="top:58px">
      <h3 class="card-title">Legacy Assets</h3>
      <p>We offer companies with mature, "non-core" assets upfront capital in exchange for products that are no longer strategic to their businesses.</p>
      <p>The partners of Northvale IP have successfully acquired over $300M of these "legacy assets", which frequently are off-patent branded generics, from large pharmaceutical companies. We have extensive experience partnering with entrepreneurial teams – typically industry executives with a deep knowledge of specific products – to acquire and manage these brands in ways that maintain and strengthen their value over time. Our focus is on products in stable markets that offer highly predictable cash flows.</p>
      <p>Our transactions enable our counterparties to invest in higher return activities such as acquiring new technologies, financing development projects, and meeting additional working capital needs.</p>
    </div>
  </article>

  <div class="abs btn">Learn More About Us</div>
</section>

<footer>
  <div class="abs footer" role="img" aria-label="Dark teal-toned photo of a suspension bridge over the bay"></div>
  <div class="abs footer-brand"><span class="brand-mark"></span><span class="brand-name">Northvale</span></div>
  <nav class="footer-nav">
    <a style="left:362px">STRATEGY</a>
    <a style="left:479px">ABOUT US</a>
    <a style="left:597px">TEAM</a>
    <a style="left:688px">NEWS</a>
    <a style="left:781px">CONTACT</a>
  </nav>
  <div class="abs legal" style="top:4828px">Northvale IP &nbsp;|&nbsp; San Francisco<br>© 2024 Northvale IP Investment Partners LLC. All Rights Reserved. &nbsp;|&nbsp; Legal Disclaimer</div>
</footer>

</body>
</html>
```